Website Name Radiant Tally

I need a website called Radiant Tally:

This site is made for: Asking people to write via Call to Action/Email about their experience regarding procedures in beauty treatments cosmetic, aesthetic and plastic surgery and doctors, clinics and institutes in certain countries/counties/etc – good and bad.
We want to find the 5 best, the 5 worst, the most effective, most ineffective, most expensive, most useless procedures and doctors, clinics, cosmetic institutes. We want to rank them and display the good and the bad, and we want to build a site which will be the base for our future projects in digital marketing for clinics, institutes and doctors. We want to build traffic, want to get data via opt in and of course we want personal opinions to feed a review site.

No complicated website just clear and easy to operate. It has to be catchy though. We are looking for a lot of traffic and we want to generate a lot of data which we want to use for future projects.

attached as word document you will find more details

```html
<!DOCTYPE html>
<html lang="en">
<head>
<meta charset="utf-8">
<title>Radiant Tally</title>
<link href="https://fonts.googleapis.com/css2?family=Ubuntu:wght@400;500;700&display=swap" rel="stylesheet">
<style>
:root{
  --navy:#0f3557;
  --teal:#5fbcbc;
  --ink:#1b1b1b;
  --line:#e6e6e6;
  --card-a:#eef3f6;
  --card-b:#fdf3e2;
  --card-c:#e6f6fa;
  --star:#f0a11c;
}
*{box-sizing:border-box;margin:0;padding:0}
html,body{width:1200px;height:3419px;overflow:hidden;background:#fff}
body{position:relative;font-family:'Ubuntu',sans-serif;color:var(--ink)}
.abs{position:absolute}
.topline{left:0;top:0;width:1200px;height:4px;background:var(--teal)}
.search{left:130px;top:29px;width:254px;height:47px;border-radius:24px;background:#e3f1ef;display:flex;align-items:center;justify-content:space-between;padding:0 18px;font-size:17px;font-weight:500;color:#2c3e4a}
.brand{font-weight:500;color:var(--navy);letter-spacing:1px;white-space:nowrap}
.brand-top{left:0;width:1200px;top:24px;text-align:center;font-size:42px}
.login{left:807px;top:41px;font-size:17px;font-weight:500;color:var(--navy)}
.vbar{left:964px;top:32px;width:2px;height:32px;background:var(--navy)}
.social{top:45px;width:12px;height:12px;border-radius:50%;background:var(--teal)}
.hdr-rule{left:0;top:93px;width:1200px;height:1px;background:var(--line)}
.nav{top:109px;font-size:17px;color:var(--ink);transform:translateX(-50%);white-space:nowrap}
.hero{left:0;top:150px;width:1200px;height:518px;
  background:
    radial-gradient(ellipse 170px 200px at 330px 230px,rgba(214,172,148,.95),rgba(214,172,148,0) 100%),
    radial-gradient(ellipse 300px 200px at 150px 520px,rgba(58,56,54,.95),rgba(58,56,54,0) 100%),
    radial-gradient(ellipse 260px 240px at 90px 200px,rgba(236,230,222,.95),rgba(236,230,222,0) 100%),
    radial-gradient(ellipse 260px 140px at 480px 420px,rgba(240,234,222,.95),rgba(240,234,222,0) 100%),
    radial-gradient(ellipse 220px 180px at 1120px 420px,rgba(245,243,239,1),rgba(245,243,239,0) 100%),
    radial-gradient(ellipse 60px 60px at 1170px 430px,rgba(250,226,170,.9),rgba(250,226,170,0) 100%),
    linear-gradient(100deg,#cfc6bd 0%,#bfb0a3 35%,#a89a8f 52%,#cfcac4 70%,#e6e3de 100%)}
.hero-disc{left:665px;top:186px;width:446px;height:446px;border-radius:50%;background:rgba(116,198,198,.85)}
.hero-text{left:665px;width:446px;text-align:center}
.welcome{top:268px;font-size:37px;color:#1f2b33}
.hero-brand{top:330px;font-size:50px;font-weight:500;color:var(--navy)}
.hero-sub{top:405px;font-size:13px;line-height:20px;color:#1f2b33;padding:0 34px}
.btn{display:flex;align-items:center;justify-content:center;gap:18px;background:var(--navy);color:#fff;border-radius:30px;font-size:20px;white-space:nowrap}
.btn svg{width:22px;height:12px}
.hero-btn{left:790px;top:470px;width:196px;height:54px;font-size:19px}
.cat{top:782px;width:324px;height:313px}
.cat-bg{position:absolute;left:0;top:0;width:100%;height:240px;border-radius:30px 30px 30px 0}
.cat-title{position:absolute;left:0;width:100%;top:22px;text-align:center;font-size:26px;font-weight:500;line-height:34px;color:#1d1d1d}
.cat-img{position:absolute;left:17px;top:110px;width:283px;height:203px;border-radius:4px}
.img-a{background:
  radial-gradient(ellipse 90px 60px at 60px 40px,rgba(90,88,86,.8),rgba(90,88,86,0) 100%),
  radial-gradient(ellipse 80px 70px at 150px 120px,rgba(222,176,150,.95),rgba(222,176,150,0) 100%),
  radial-gradient(ellipse 70px 90px at 220px 110px,rgba(250,250,248,1),rgba(250,250,248,0) 100%),
  linear-gradient(160deg,#b9c2c8 0%,#e3ddd6 55%,#f2efea 100%)}
.img-b{background:
  radial-gradient(ellipse 90px 80px at 90px 60px,rgba(40,30,28,.95),rgba(40,30,28,0) 100%),
  radial-gradient(ellipse 120px 70px at 170px 110px,rgba(214,168,140,.95),rgba(214,168,140,0) 100%),
  radial-gradient(ellipse 160px 50px at 150px 190px,rgba(248,248,246,1),rgba(248,248,246,0) 100%),
  linear-gradient(150deg,#cdbdb1 0%,#e6ddd5 60%,#f4f2f0 100%)}
.img-c{background:
  radial-gradient(ellipse 80px 90px at 70px 70px,rgba(238,240,242,1),rgba(238,240,242,0) 100%),
  radial-gradient(ellipse 110px 100px at 180px 120px,rgba(224,172,142,.95),rgba(224,172,142,0) 100%),
  radial-gradient(ellipse 60px 100px at 260px 100px,rgba(150,112,80,.8),rgba(150,112,80,0) 100%),
  linear-gradient(150deg,#6e7478 0%,#bfb4ac 45%,#d9c3b1 100%)}
.about-h{left:104px;top:1250px;font-size:44px;font-weight:500}
.rule{height:4px;background:var(--teal)}
.about-p{left:104px;width:494px;font-size:15.5px;line-height:26px;color:#4a4a4a}
.about-img{left:641px;top:1245px;width:445px;height:588px;border-radius:223px 223px 0 0;
  background:
    radial-gradient(ellipse 80px 90px at 230px 120px,rgba(214,170,146,.95),rgba(214,170,146,0) 100%),
    radial-gradient(ellipse 70px 90px at 180px 110px,rgba(110,76,58,.85),rgba(110,76,58,0) 100%),
    radial-gradient(ellipse 200px 260px at 250px 400px,rgba(246,243,236,1),rgba(246,243,236,0) 100%),
    radial-gradient(ellipse 130px 300px at 40px 250px,rgba(150,166,160,.9),rgba(150,166,160,0) 100%),
    radial-gradient(ellipse 120px 200px at 420px 200px,rgba(190,204,170,.8),rgba(190,204,170,0) 100%),
    linear-gradient(160deg,#aab6b2 0%,#dcd8cf 50%,#cfc7bc 100%)}
.about-arc{left:641px;top:1245px;width:459px;height:588px;border-radius:230px 230px 0 0;border:14px solid var(--teal);border-left:none;border-bottom:none}
.band{left:0;top:1833px;width:1200px;height:521px;
  background:
    radial-gradient(ellipse 300px 160px at 400px 300px,rgba(62,140,142,.55),rgba(62,140,142,0) 100%),
    radial-gradient(ellipse 260px 140px at 250px 440px,rgba(72,150,152,.5),rgba(72,150,152,0) 100%),
    radial-gradient(ellipse 200px 200px at 1000px 120px,rgba(140,210,208,.6),rgba(140,210,208,0) 100%),
    radial-gradient(ellipse 200px 140px at 900px 430px,rgba(84,164,164,.5),rgba(84,164,164,0) 100%),
    linear-gradient(120deg,#73c5c4 0%,#63b7b6 45%,#76c6c5 100%)}
.band-h{left:0;width:1200px;top:1914px;text-align:center;font-size:43px;font-weight:500;line-height:53px;color:#13202a}
.test-h{left:104px;top:2455px;font-size:44px;font-weight:500}
.arrows{left:1016px;top:2451px;width:96px;height:61px;background:#f1f5f6;border-radius:4px}
.card{top:2589px;width:268px;height:295px;background:#fff;border:1px solid #e4e4e4;border-radius:4px;padding:16px 17px}
.card.lift{top:2617px;box-shadow:0 6px 22px rgba(0,0,0,.12);border-color:transparent}
.stars{display:flex;align-items:center;gap:3px;font-size:14px;color:#777}
.stars svg{width:15px;height:15px;fill:var(--star)}
.quote{margin-top:20px;font-size:12.5px;line-height:19px;color:#8a8a8a}
.who{margin-top:20px;display:flex;align-items:center;gap:14px}
.avatar{width:60px;height:60px;border-radius:50%;border:2px solid #333;background:radial-gradient(circle at 50% 40%,#d9b39a 0,#a37f6a 35%,#3e3330 100%)}
.who b{display:block;font-weight:500;font-size:19px;color:#1d1d1d}
.who span{font-size:13px;color:#666}
.foot-rule{left:96px;top:3005px;width:1004px;height:2px;background:var(--teal)}
.brand-foot{left:0;width:1200px;top:3070px;text-align:center;font-size:42px}
.fnav{top:3164px;font-size:17px;transform:translateX(-50%);white-space:nowrap}
.ficon{top:3228px;width:60px;height:60px;border-radius:50%;background:linear-gradient(160deg,#1d5a73,#5fbcbc);display:flex;align-items:center;justify-content:center}
.ficon svg{width:26px;height:26px}
.flabel{font-size:15px;color:#333}
.fval{font-size:17px;line-height:25px;color:#1d1d1d}
.foot-bottom{left:122px;top:3333px;width:971px;height:1px;background:var(--line)}
.copy{left:0;width:1200px;top:3362px;text-align:center;font-size:17px;color:#222}
</style>
</head>
<body>
<div class="abs topline"></div>

<div class="abs search"><span>Search</span>
<svg width="16" height="16" viewBox="0 0 16 16"><circle cx="6.5" cy="6.5" r="4.8" fill="none" stroke="#0f3557" stroke-width="2.2"/><line x1="10" y1="10" x2="14.5" y2="14.5" stroke="#0f3557" stroke-width="2.4"/></svg></div>
<div class="abs brand brand-top">RADIANT TALLY</div>
<div class="abs login">Login or Register</div>
<div class="abs vbar"></div>
<svg class="abs" style="left:979px;top:43px" width="16" height="16" viewBox="0 0 16 16"><circle cx="6.5" cy="6.5" r="4.8" fill="none" stroke="#5fbcbc" stroke-width="2"/><line x1="10" y1="10" x2="14.5" y2="14.5" stroke="#5fbcbc" stroke-width="2.2"/></svg>
<div class="abs social" style="left:1015px"></div>
<div class="abs social" style="left:1049px"></div>
<div class="abs hdr-rule"></div>

<div class="abs nav" style="left:219px">Home</div>
<div class="abs nav" style="left:345px">About Us</div>
<div class="abs nav" style="left:480px">Services</div>
<div class="abs nav" style="left:638px">Why Choose Us</div>
<div class="abs nav" style="left:809px">Experience</div>
<div class="abs nav" style="left:962px">Contact Us</div>

<div class="abs hero" role="img" aria-label="Photo of a relaxed woman lying on a sofa beside spa towels and candles"></div>
<div class="abs hero-disc"></div>
<div class="abs hero-text welcome">Welcome to</div>
<div class="abs hero-text hero-brand">RADIANT TALLY</div>
<div class="abs hero-text hero-sub">Sed ut perspiciatis unde omnis iste natus error sit voluptatem accusantium doloremque laudantium, totam rem</div>
<div class="abs btn hero-btn">Get Started <svg viewBox="0 0 22 12"><path d="M0 6h18M13 1l6 5-6 5" fill="none" stroke="#fff" stroke-width="2.4"/></svg></div>

<div class="abs cat" style="left:98px"><div class="cat-bg" style="background:var(--card-a)"></div><div class="cat-title">Aesthetic Medicine<br>Treatments</div><div class="cat-img img-a" role="img" aria-label="Photo of a facial laser treatment"></div></div>
<div class="abs cat" style="left:438px"><div class="cat-bg" style="background:var(--card-b)"></div><div class="cat-title">Medical Cosmetic<br>Treatments</div><div class="cat-img img-b" role="img" aria-label="Photo of a woman reclining on white sheets"></div></div>
<div class="abs cat" style="left:778px"><div class="cat-bg" style="background:var(--card-c)"></div><div class="cat-title">Aesthetic &amp; Plastic<br>Surgery</div><div class="cat-img img-c" role="img" aria-label="Photo of a cosmetic injection procedure"></div></div>

<div class="abs about-h">About Us</div>
<div class="abs rule" style="left:104px;top:1320px;width:123px"></div>
<p class="abs about-p" style="top:1352px">Lorem ipsum dolor sit amet, consectetur adipiscing elit, sed do eiusmod tempor incididunt ut labore et dolore magna aliqua. Ut enim ad minim veniam, quis nostrud exercitation ullamco laboris nisi ut aliquip ex ea commodo consequat. Duis aute irure dolor in reprehenderit in voluptate velit esse cillum dolore eu fugiat nulla pariatur. Excepteur sint occaecat cupidatat non proident, sunt in culpa qui officia deserunt mollit anim id est laborum</p>
<p class="abs about-p" style="top:1560px">Lorem ipsum dolor sit amet, consectetur adipiscing elit, sed do eiusmod tempor incididunt ut labore et dolore magna aliqua. Ut enim ad minim veniam, quis nostrud exercitation ullamco laboris nisi ut aliquip ex ea commodo consequat.</p>
<div class="abs btn" style="left:104px;top:1693px;width:196px;height:56px">Read More <svg viewBox="0 0 22 12"><path d="M0 6h18M13 1l6 5-6 5" fill="none" stroke="#fff" stroke-width="2.4"/></svg></div>
<div class="abs about-arc"></div>
<div class="abs about-img" role="img" aria-label="Photo of a smiling woman in white sitting by a window"></div>

<div class="abs band" role="img" aria-label="Teal-tinted photo of a woman receiving a facial treatment"></div>
<div class="abs band-h">Write us Your Experience<br>of The Best</div>
<div class="abs rule" style="left:537px;top:2038px;width:123px"></div>
<div class="abs btn" style="left:369px;top:2094px;width:195px;height:55px">Worst <svg viewBox="0 0 22 12"><path d="M0 6h18M13 1l6 5-6 5" fill="none" stroke="#fff" stroke-width="2.4"/></svg></div>
<div class="abs btn" style="left:589px;top:2094px;width:242px;height:55px">Most Effective <svg viewBox="0 0 22 12"><path d="M0 6h18M13 1l6 5-6 5" fill="none" stroke="#fff" stroke-width="2.4"/></svg></div>
<div class="abs btn" style="left:289px;top:2195px;width:240px;height:55px">Most Useless <svg viewBox="0 0 22 12"><path d="M0 6h18M13 1l6 5-6 5" fill="none" stroke="#fff" stroke-width="2.4"/></svg></div>
<div class="abs btn" style="left:555px;top:2193px;width:355px;height:55px">Most Expensive Procedure <svg viewBox="0 0 22 12"><path d="M0 6h18M13 1l6 5-6 5" fill="none" stroke="#fff" stroke-width="2.4"/></svg></div>

<div class="abs test-h">What Our Customer Says</div>
<div class="abs rule" style="left:104px;top:2525px;width:123px"></div>
<div class="abs arrows">
<svg class="abs" style="left:14px;top:24px" width="24" height="12" viewBox="0 0 24 12"><path d="M24 6H3M8 1L2 6l6 5" fill="none" stroke="#9aa" stroke-width="1.6"/></svg>
<svg class="abs" style="left:51px;top:14px" width="33" height="33" viewBox="0 0 33 33"><circle cx="16.5" cy="16.5" r="16.5" fill="#5fbcbc"/><path d="M8 16.5h16M19 11.5l5.5 5-5.5 5" fill="none" stroke="#fff" stroke-width="2"/></svg>
</div>

<div class="abs card" style="left:98px">
<div class="stars"><svg viewBox="0 0 20 20"><path d="M10 1l2.7 6 6.3.6-4.8 4.2 1.4 6.2L10 14.8 4.4 18l1.4-6.2L1 7.6l6.3-.6z"/></svg><svg viewBox="0 0 20 20"><path d="M10 1l2.7 6 6.3.6-4.8 4.2 1.4 6.2L10 14.8 4.4 18l1.4-6.2L1 7.6l6.3-.6z"/></svg><svg viewBox="0 0 20 20"><path d="M10 1l2.7 6 6.3.6-4.8 4.2 1.4 6.2L10 14.8 4.4 18l1.4-6.2L1 7.6l6.3-.6z"/></svg><svg viewBox="0 0 20 20"><path d="M10 1l2.7 6 6.3.6-4.8 4.2 1.4 6.2L10 14.8 4.4 18l1.4-6.2L1 7.6l6.3-.6z"/></svg><svg viewBox="0 0 20 20"><path d="M10 1l2.7 6 6.3.6-4.8 4.2 1.4 6.2L10 14.8 4.4 18l1.4-6.2L1 7.6l6.3-.6z"/></svg> (5)</div>
<p class="quote">Nemo enim ipsam voluptatem quia voluptas sit aspernatur aut odit aut fugit, sed quia consequuntur magni dolores eos qui ratione voluptatem sequi nesciunt. Neque porro quisquam est, qui dolorem ipsum quia dolor sit amet, consectetur.</p>
<div class="who"><div class="avatar" role="img" aria-label="Customer portrait"></div><div><b>Eaque ipsa</b><span>Washington</span></div></div>
</div>

<div class="abs card lift" style="left:401px">
<div class="stars"><svg viewBox="0 0 20 20"><path d="M10 1l2.7 6 6.3.6-4.8 4.2 1.4 6.2L10 14.8 4.4 18l1.4-6.2L1 7.6l6.3-.6z"/></svg><svg viewBox="0 0 20 20"><path d="M10 1l2.7 6 6.3.6-4.8 4.2 1.4 6.2L10 14.8 4.4 18l1.4-6.2L1 7.6l6.3-.6z"/></svg><svg viewBox="0 0 20 20"><path d="M10 1l2.7 6 6.3.6-4.8 4.2 1.4 6.2L10 14.8 4.4 18l1.4-6.2L1 7.6l6.3-.6z"/></svg><svg viewBox="0 0 20 20"><path d="M10 1l2.7 6 6.3.6-4.8 4.2 1.4 6.2L10 14.8 4.4 18l1.4-6.2L1 7.6l6.3-.6z"/></svg><svg viewBox="0 0 20 20"><path d="M10 1l2.7 6 6.3.6-4.8 4.2 1.4 6.2L10 14.8 4.4 18l1.4-6.2L1 7.6l6.3-.6z"/></svg> (5)</div>
<p class="quote">Nemo enim ipsam voluptatem quia voluptas sit aspernatur aut odit aut fugit, sed quia consequuntur magni dolores eos qui ratione voluptatem sequi nesciunt. Neque porro quisquam est, qui dolorem ipsum quia dolor sit amet, consectetur.</p>
<div class="who"><div class="avatar" role="img" aria-label="Customer portrait" style="background:radial-gradient(circle at 50% 40%,#f0d2b4 0,#d7a84f 40%,#8a6a3a 100%)"></div><div><b>Eaque ipsa</b><span>Washington</span></div></div>
</div>

<div class="abs card" style="left:701px">
<div class="stars"><svg viewBox="0 0 20 20"><path d="M10 1l2.7 6 6.3.6-4.8 4.2 1.4 6.2L10 14.8 4.4 18l1.4-6.2L1 7.6l6.3-.6z"/></svg><svg viewBox="0 0 20 20"><path d="M10 1l2.7 6 6.3.6-4.8 4.2 1.4 6.2L10 14.8 4.4 18l1.4-6.2L1 7.6l6.3-.6z"/></svg><svg viewBox="0 0 20 20"><path d="M10 1l2.7 6 6.3.6-4.8 4.2 1.4 6.2L10 14.8 4.4 18l1.4-6.2L1 7.6l6.3-.6z"/></svg><svg viewBox="0 0 20 20"><path d="M10 1l2.7 6 6.3.6-4.8 4.2 1.4 6.2L10 14.8 4.4 18l1.4-6.2L1 7.6l6.3-.6z"/></svg><svg viewBox="0 0 20 20"><path d="M10 1l2.7 6 6.3.6-4.8 4.2 1.4 6.2L10 14.8 4.4 18l1.4-6.2L1 7.6l6.3-.6z"/></svg> (5)</div>
<p class="quote">Nemo enim ipsam voluptatem quia voluptas sit aspernatur aut odit aut fugit, sed quia consequuntur magni dolores eos qui ratione voluptatem sequi nesciunt. Neque porro quisquam est, qui dolorem ipsum quia dolor sit amet, consectetur.</p>
<div class="who"><div class="avatar" role="img" aria-label="Customer portrait" style="background:radial-gradient(circle at 50% 40%,#e4c2a8 0,#b08a72 35%,#4a3a34 100%)"></div><div><b>Eaque ipsa</b><span>Washington</span></div></div>
</div>

<div class="abs card" style="left:1002px">
<div class="stars"><svg viewBox="0 0 20 20"><path d="M10 1l2.7 6 6.3.6-4.8 4.2 1.4 6.2L10 14.8 4.4 18l1.4-6.2L1 7.6l6.3-.6z"/></svg><svg viewBox="0 0 20 20"><path d="M10 1l2.7 6 6.3.6-4.8 4.2 1.4 6.2L10 14.8 4.4 18l1.4-6.2L1 7.6l6.3-.6z"/></svg><svg viewBox="0 0 20 20"><path d="M10 1l2.7 6 6.3.6-4.8 4.2 1.4 6.2L10 14.8 4.4 18l1.4-6.2L1 7.6l6.3-.6z"/></svg><svg viewBox="0 0 20 20"><path d="M10 1l2.7 6 6.3.6-4.8 4.2 1.4 6.2L10 14.8 4.4 18l1.4-6.2L1 7.6l6.3-.6z"/></svg><svg viewBox="0 0 20 20"><path d="M10 1l2.7 6 6.3.6-4.8 4.2 1.4 6.2L10 14.8 4.4 18l1.4-6.2L1 7.6l6.3-.6z"/></svg> (5)</div>
<p class="quote">Nemo enim ipsam voluptatem quia voluptas sit aspernatur aut odit aut fugit, sed quia consequuntur magni dolores eos qui ratione voluptatem sequi nesciunt. Neque porro quisquam est, qui dolorem ipsum quia dolor sit amet, consectetur.</p>
<div class="who"><div class="avatar" role="img" aria-label="Customer portrait" style="background:radial-gradient(circle at 50% 40%,#8a6450 0,#5a3e34 40%,#1f2a4a 100%)"></div><div><b>Eaque ipsa</b><span>Washington</span></div></div>
</div>

<div class="abs foot-rule"></div>
<div class="abs brand brand-foot">RADIANT TALLY</div>
<div class="abs fnav" style="left:248px">Home</div>
<div class="abs fnav" style="left:374px">About Us</div>
<div class="abs fnav" style="left:510px">Services</div>
<div class="abs fnav" style="left:669px">Why Choose Us</div>
<div class="abs fnav" style="left:839px">Experience</div>
<div class="abs fnav" style="left:991px">Contact Us</div>

<div class="abs ficon" style="left:177px"><svg viewBox="0 0 24 24"><path d="M12 2a7 7 0 0 0-7 7c0 5 7 13 7 13s7-8 7-13a7 7 0 0 0-7-7z" fill="none" stroke="#fff" stroke-width="2"/><circle cx="12" cy="9" r="2.5" fill="#fff"/></svg></div>
<div class="abs" style="left:260px;top:3228px"><div class="flabel">Address</div><div class="fval">1254 Nemo enim ipsam<br>voluptatem 12542</div></div>

<div class="abs ficon" style="left:522px"><svg viewBox="0 0 24 24"><path d="M6.6 10.8a15 15 0 0 0 6.6 6.6l2.2-2.2c.3-.3.7-.4 1-.2 1.1.4 2.3.6 3.6.6.6 0 1 .4 1 1V20c0 .6-.4 1-1 1A17 17 0 0 1 3 4c0-.6.4-1 1-1h3.5c.6 0 1 .4 1 1 0 1.3.2 2.5.6 3.6.1.3 0 .7-.2 1z" fill="#fff"/></svg></div>
<div class="abs" style="left:605px;top:3228px"><div class="flabel">Phone</div><div class="fval">+1 555-010-2024</div></div>

<div class="abs ficon" style="left:805px"><svg viewBox="0 0 24 24"><rect x="2.5" y="5" width="19" height="14" rx="1.5" fill="none" stroke="#fff" stroke-width="2"/><path d="M3 6l9 7 9-7" fill="none" stroke="#fff" stroke-width="2"/></svg></div>
<div class="abs" style="left:882px;top:3228px"><div class="flabel">Email</div><div class="fval" style="margin-top:3px">info@radianttally.com</div></div>

<div class="abs foot-bottom"></div>
<div class="abs copy">© copyrights 2023&nbsp; Radiant Tally.&nbsp; All Rights Reserved</div>
</body>
</html>
```